Pelkman Agency (http://pa.quorvexstudio.com/)

We are looking for a similar design to what we have, but more professional looking and cleaned up with links and logo that is not so grainy looking. We are an independent insurance agency marketing to personal and commercial clients. We offer all commercial lines markets and all personal lines. We target excavators, landscapers, restaurants, golf courses, contractors. Please look at http://pa.quorvexstudio.com/ which we had designed but do not like it, it will give you an idea of what we are looking for.

Target Market(s)

Commercial and personal insurance. All business products and all personal (homeowners, auto, antique auto, umbrella)

Industry/Entity Type

It Professional

Logo Text

Knowledge Building Your Assurance

Number of Pages Required

5+ page

Colors
000000
848484
0255a3

```html
<!DOCTYPE html>
<html lang="en">
<head>
<meta charset="utf-8">
<title>Pelkman Agency</title>
<link href="https://fonts.googleapis.com/css2?family=Open+Sans:wght@300;400;600;700&display=swap" rel="stylesheet">
<style>
  :root {
    --black: #000000;
    --grey: #848484;
    --blue: #0255a3;
    --white: #ffffff;
    --text: #222222;
    --rule: #d8d8d8;
  }
  * { box-sizing: border-box; margin: 0; padding: 0; }
  html, body { width: 761px; height: 1200px; overflow: hidden; background: var(--white); }
  body { position: relative; font-family: "Open Sans", Arial, sans-serif; color: var(--text); }

  .site-header { position: absolute; left: 5px; top: 0; width: 752px; height: 84px; background: var(--black); }
  .brand { position: absolute; left: 30px; top: 10px; font-size: 33px; font-weight: 700; color: var(--white); letter-spacing: -0.5px; }
  .call-box { position: absolute; left: 337px; top: 21px; width: 245px; height: 28px; background: var(--blue); border-radius: 3px;
    color: var(--white); font-size: 15px; font-weight: 600; line-height: 28px; text-align: center; }
  .social { position: absolute; right: 24px; top: 28px; display: flex; gap: 6px; }
  .social span { width: 17px; height: 17px; border-radius: 50%; background: var(--grey); }
  .social span:first-child { background: var(--blue); }
  .main-nav { position: absolute; left: 29px; top: 62px; display: flex; font-size: 9.5px; font-weight: 600; color: var(--white); }
  .main-nav a { color: inherit; text-decoration: none; }
  .main-nav a.active { color: #4d9be6; }
  .main-nav .sep { margin: 0 13px; }

  .hero { position: absolute; left: 5px; top: 84px; width: 752px; height: 310px;
    background: linear-gradient(180deg, #bfe3f4 0%, #7fbf5a 45%, #3f8c2e 75%, #4aa6c8 100%); }
  .hero-caption { position: absolute; left: 145px; top: 197px; width: 460px; height: 60px; background: rgba(150,200,90,0.55);
    font-size: 50px; font-weight: 300; color: #1a1a1a; line-height: 60px; text-align: center; }
  .hero-arrow { position: absolute; top: 140px; }
  .hero-dots { position: absolute; left: 359px; top: 290px; display: flex; gap: 5px; }
  .hero-dots span { width: 7px; height: 7px; border-radius: 50%; background: rgba(255,255,255,0.6); }
  .hero-dots span:first-child { background: var(--white); }

  .intro-title { position: absolute; left: 0; top: 409px; width: 761px; text-align: center; font-size: 20px; color: var(--blue); }
  .intro-text { position: absolute; left: 0; top: 438px; width: 761px; text-align: center; font-size: 13px; color: var(--text); }

  .service { position: absolute; width: 338px; }
  .service-image { width: 338px; height: 193px; position: relative; }
  .service-title { margin-top: 14px; text-align: center; font-size: 20px; font-weight: 400; color: var(--text); }
  .service-text { margin-top: 10px; font-size: 10.5px; line-height: 14.7px; color: var(--grey); text-align: justify; text-align-last: center; font-weight: 300; }
  .quote-btn { position: absolute; left: 115px; top: 84px; width: 108px; height: 28px; background: rgba(40,40,40,0.75); border-radius: 3px;
    color: var(--white); font-size: 11px; line-height: 28px; display: flex; align-items: center; gap: 8px; padding-left: 10px; }

  .footer-rule { position: absolute; left: 5px; top: 1126px; width: 752px; height: 1px; background: var(--rule); }
  .footer-nav { position: absolute; left: 0; top: 1146px; width: 761px; display: flex; justify-content: center; font-size: 9.5px; color: var(--text); }
  .footer-nav .active { color: var(--blue); }
  .footer-nav .sep { margin: 0 13px; }
  .copyright { position: absolute; left: 0; top: 1175px; width: 761px; text-align: center; font-size: 8.5px; color: var(--grey); }
</style>
</head>
<body>
  <header class="site-header">
    <div class="brand">Pelkman Agency</div>
    <div class="call-box">CALL US TODAY: 1-888-4 PELKMN</div>
    <div class="social"><span></span><span></span><span></span></div>
    <nav class="main-nav">
      <a class="active">HOME</a><span class="sep">|</span>
      <a>PERSONAL INSURANCE</a><span class="sep">|</span>
      <a>BUSINESS INSURANCE</a><span class="sep">|</span>
      <a>SERVICE CENTER</a><span class="sep">|</span>
      <a>ABOUT US</a><span class="sep">|</span>
      <a>CONTACT US</a>
    </nav>
  </header>

  <section class="hero" role="img" aria-label="Large yellow house with garden lawn and pond">
    <svg class="hero-arrow" style="left:6px" width="14" height="24" viewBox="0 0 14 24"><path d="M11 2 L3 12 L11 22" fill="none" stroke="rgba(255,255,255,0.7)" stroke-width="3"/></svg>
    <svg class="hero-arrow" style="right:6px" width="14" height="24" viewBox="0 0 14 24"><path d="M3 2 L11 12 L3 22" fill="none" stroke="rgba(255,255,255,0.7)" stroke-width="3"/></svg>
    <div class="hero-caption">Property Insurance</div>
    <div class="hero-dots"><span></span><span></span><span></span></div>
  </section>

  <h1 class="intro-title">SMALL ENOUGH TO CARE, BIG ENOUGH TO MAKE A DIFFERENCE</h1>
  <p class="intro-text">Please find information about our agency, its principles , and the various types of insurance coverages that we provide.</p>

  <article class="service" style="left:35px; top:474px;">
    <div class="service-image" role="img" aria-label="Two businessmen under a red umbrella in a meadow" style="background:linear-gradient(180deg,#9cc6ec 0%,#dfeaf2 50%,#b9b44a 70%,#6f7d2a 100%);">
      <div class="quote-btn">
        <svg width="14" height="14" viewBox="0 0 14 14"><rect x="2" y="1" width="9" height="12" fill="none" stroke="#fff" stroke-width="1.3"/><path d="M4 5h5M4 8h5" stroke="#fff" stroke-width="1.2"/></svg>
        GET A QUOTE
      </div>
    </div>
    <h2 class="service-title">BUSINEES INSURENCE</h2>
    <p class="service-text">Lorem Ipsum is simply dummy text of the printing and typesetting industry. Lorem Ipsum has been the industry's standard dummy text ever since the 1500s, when an unknown printer took a galley of type and scrambled it to make a type specimen book.</p>
  </article>

  <article class="service" style="left:389px; top:474px;">
    <div class="service-image" role="img" aria-label="Hands holding a small blue toy car" style="background:linear-gradient(135deg,#2a2a2a 0%,#6b5a50 45%,#c89a82 70%,#3a3a3a 100%);"></div>
    <h2 class="service-title">AUTO INSURENCE</h2>
    <p class="service-text">Lorem Ipsum is simply dummy text of the printing and typesetting industry. Lorem Ipsum has been the industry's standard dummy text ever since the 1500s, when an unknown printer took a galley of type and scrambled it to make a type specimen book.</p>
  </article>

  <article class="service" style="left:35px; top:790px;">
    <div class="service-image" role="img" aria-label="Family walking hand in hand across a lawn" style="background:linear-gradient(180deg,#4a8fe0 0%,#a9cdef 45%,#6ea447 75%,#3f7a2a 100%);"></div>
    <h2 class="service-title">LIFE INSURENCE</h2>
    <p class="service-text">Lorem Ipsum is simply dummy text of the printing and typesetting industry. Lorem Ipsum has been the industry's standard dummy text ever since the 1500s, when an unknown printer took a galley of type and scrambled it to make a type specimen book.</p>
  </article>

  <article class="service" style="left:389px; top:790px;">
    <div class="service-image" role="img" aria-label="Cupped hands holding a small model house" style="background:linear-gradient(180deg,#f2f2f2 0%,#e2d6c8 55%,#e8c2a6 80%,#f0ece8 100%);"></div>
    <h2 class="service-title">HOME INSURENCE</h2>
    <p class="service-text">Lorem Ipsum is simply dummy text of the printing and typesetting industry. Lorem Ipsum has been the industry's standard dummy text ever since the 1500s, when an unknown printer took a galley of type and scrambled it to make a type specimen book.</p>
  </article>

  <div class="footer-rule"></div>
  <nav class="footer-nav">
    <span class="active">HOME</span><span class="sep">|</span>
    <span>PERSONAL INSURANCE</span><span class="sep">|</span>
    <span>BUSINESS INSURANCE</span><span class="sep">|</span>
    <span>SERVICE CENTER</span><span class="sep">|</span>
    <span>ABOUT US</span><span class="sep">|</span>
    <span>CONTACT US</span>
  </nav>
  <p class="copyright">© 2015 pelkman agency, All rights reserved.</p>
</body>
</html>
```